PRICE LIST

I wont a design similar to my business card but not black i wont it very easy to read and simple here is my price list so far

Industry/Entity Type

Business

Font styles to use
Script

```html
<!DOCTYPE html>
<html lang="en">
<head>
<meta charset="utf-8">
<title>Simple Glow – Price List</title>
<link rel="stylesheet" href="https://fonts.googleapis.com/css2?family=Josefin+Sans:wght@300;400;600;700&family=Cinzel:wght@400&family=Didact+Gothic&display=swap">
<style>
  :root {
    --red: #e8383f;
    --ink: #1d1d1d;
    --muted: #333333;
    --paper: #ffffff;
    --board: #ffffff;
    --badge: #e6e6e6;
    --shadow: rgba(0,0,0,0.28);
  }
  * { box-sizing: border-box; margin: 0; padding: 0; }
  html, body { width: 1200px; height: 849px; overflow: hidden; background: var(--board); }
  body { position: relative; font-family: "Josefin Sans", sans-serif; color: var(--ink); }

  .board-label { position: absolute; left: 63px; top: 24px; font: 22px "Didact Gothic", sans-serif; color: var(--ink); }
  .board-title { position: absolute; left: 0; width: 1170px; top: 56px; text-align: center; font: 22px "Didact Gothic", sans-serif; color: var(--ink); }

  .sheet {
    position: absolute; left: 339px; top: 95px; width: 490px; height: 694px;
    background: var(--paper); border: 1px solid #8a8a8a;
    box-shadow: 6px 7px 6px var(--shadow);
  }
  .abs { position: absolute; white-space: nowrap; }

  .brand-name { left: 0; width: 490px; top: 38px; text-align: center; font-weight: 700; font-size: 46px; color: var(--red); letter-spacing: -0.5px; }
  .brand-sub { left: 206px; width: 150px; top: 84px; text-align: right; font-weight: 700; font-size: 20px; color: var(--red); }

  .rule { position: absolute; height: 1.5px; background: var(--red); }
  .rule-end { position: absolute; width: 8px; height: 8px; border-radius: 50%; background: var(--red); }

  .oval {
    position: absolute; border: 2px solid var(--red); border-radius: 50%; background: var(--paper);
    display: flex; flex-direction: column; align-items: center; justify-content: center; text-align: center;
  }
  .oval--therapist { left: 81px; top: 103px; width: 112px; height: 60px; font: 10.5px/1.05 "Cinzel", serif; color: var(--ink); }
  .oval--hours { left: 301px; top: 579px; width: 106px; height: 74px; font: 600 11.5px/1.1 "Josefin Sans", sans-serif; letter-spacing: 0.5px; }

  .contact { font-weight: 600; font-size: 10.5px; color: var(--ink); }
  .partner { position: absolute; top: 146px; height: 24px; border-radius: 4px; background: var(--badge); }

  .heading { font-weight: 600; font-size: 15px; color: var(--ink); }
  .item { display: flex; align-items: baseline; font-weight: 300; font-size: 13.5px; }
  .item .leader { flex: 1; border-bottom: 1px dotted #777; margin: 0 2px; transform: translateY(-3px); }
  .item .price { font-weight: 400; }
  .col-left { left: 50px; width: 190px; }
  .col-right { left: 278px; width: 156px; }
  .desc { font-weight: 400; font-size: 9.5px; color: var(--muted); }
  .addon { font-size: 10px; text-align: right; }
  .addon b { font-weight: 400; font-size: 13px; }

  .new-tag {
    left: 414px; top: 459px; width: 42px; height: 26px; border-radius: 50%;
    background: var(--red); color: #fff; font-weight: 700; font-size: 11px;
    display: flex; align-items: center; justify-content: center; transform: rotate(-10deg);
  }

  .social-icon { display: inline-block; width: 14px; height: 14px; background: var(--red); vertical-align: -3px; margin-right: 3px; }
  .social-icon--round { border-radius: 50%; }

  .ornament-area { position: absolute; left: 896px; top: 290px; width: 196px; height: 312px; background: var(--red); border-radius: 40px; }
</style>
</head>
<body>
  <div class="board-label">Simple Glow</div>
  <div class="board-title">Price List - one - colour option</div>

  <main class="sheet">
    <div class="abs brand-name">Simple Glow</div>
    <div class="abs brand-sub">Home Salon</div>

    <div class="rule-end" style="left:29px;top:129px"></div>
    <div class="rule" style="left:33px;top:132px;width:422px"></div>
    <div class="rule-end" style="left:453px;top:129px"></div>
    <div class="oval oval--therapist">QUALIFIED<br>BEAUTY<br>THERAPIST</div>
    <div class="abs contact" style="left:212px;top:118px">Palm Reach, Sunny Bay | Ph: 0400 123 987</div>

    <div class="partner" style="left:197px;width:74px"></div>
    <div class="partner" style="left:287px;width:78px"></div>
    <div class="partner" style="left:378px;width:60px"></div>

    <section>
      <div class="abs heading col-left" style="top:205px">Manicures &amp; Pedicures</div>

      <div class="abs item col-left" style="top:228px"><span>Gel Shine Manicure</span><span class="leader"></span><span class="price">$30</span></div>
      <div class="abs desc col-left" style="top:246px">Cut, shape, cuticles &amp; Gel Shine</div>

      <div class="abs item col-left" style="top:268px"><span>Deluxe Manicure</span><span class="leader"></span><span class="price">$40</span></div>
      <div class="abs desc col-left" style="top:286px">Soak, exfoliate, cut, shape, cuticles &amp; polish</div>
      <div class="abs addon col-left" style="top:299px">Add Gel Shine <b>$10</b></div>

      <div class="abs item col-left" style="top:323px"><span>Paraffin Manicure</span><span class="leader"></span><span class="price">$45</span></div>
      <div class="abs desc col-left" style="top:341px">Soak, exfoliate, paraffin treatment, cut,</div>
      <div class="abs desc col-left" style="top:357px">shape, cuticles &amp; polish</div>
      <div class="abs addon col-left" style="top:369px">Add Gel Shine <b>&nbsp;$5</b></div>

      <div class="abs item col-left" style="top:394px"><span>Gel Shine Pedicure</span><span class="leader"></span><span class="price">$30</span></div>
      <div class="abs desc col-left" style="top:412px">Cut, shape, cuticles &amp; Gel Shine</div>

      <div class="abs item col-left" style="top:434px"><span>Deluxe Pedicure</span><span class="leader"></span><span class="price">$40</span></div>
      <div class="abs desc col-left" style="top:452px">Soak, exfoliate, cut, shape, cuticles &amp; polish</div>
      <div class="abs addon col-left" style="top:465px">Add Gel Shine <b>$10</b></div>

      <div class="abs item col-left" style="top:489px"><span>Paraffin Pedicure</span><span class="leader"></span><span class="price">$45</span></div>
      <div class="abs desc col-left" style="top:507px">Soak, exfoliate, paraffin treatment, cut,</div>
      <div class="abs desc col-left" style="top:523px">shape, cuticles &amp; polish</div>
      <div class="abs addon col-left" style="top:536px">Add Gel Shine <b>&nbsp;$5</b></div>
    </section>

    <section>
      <div class="abs heading col-right" style="top:205px">Waxing</div>
      <div class="abs item col-right" style="top:228px"><span>Eyebrows Wax</span><span class="leader"></span><span class="price">$10</span></div>
      <div class="abs item col-right" style="top:252px"><span>Lip Wax</span><span class="leader"></span><span class="price">$10</span></div>
      <div class="abs item col-right" style="top:277px"><span>Chin Wax</span><span class="leader"></span><span class="price">$10</span></div>
      <div class="abs item col-right" style="top:302px"><span>Underarms Wax</span><span class="leader"></span><span class="price">$10</span></div>

      <div class="abs heading col-right" style="top:360px">Tinting</div>
      <div class="abs item col-right" style="top:383px"><span>Eyebrows Tint</span><span class="leader"></span><span class="price">$10</span></div>
      <div class="abs item col-right" style="top:407px"><span>Eyelashes Tint</span><span class="leader"></span><span class="price">$10</span></div>

      <div class="abs heading col-right" style="top:465px">Tanning</div>
      <div class="abs new-tag">NEW!</div>
      <div class="abs item col-right" style="top:488px"><span>GLOW TAN</span><span class="leader"></span><span class="price">$25</span></div>
      <div class="abs desc col-right" style="top:506px">Very popular UV-Free 2-hour session</div>
      <div class="abs desc col-right" style="top:521px">is available in all ranges (suitable for</div>
      <div class="abs desc col-right" style="top:536px">all skin types)</div>
    </section>

    <footer>
      <div class="abs contact" style="left:57px;top:601px;font-size:9.5px">Check out my social media pages:</div>
      <div class="rule-end" style="left:29px;top:612px"></div>
      <div class="rule" style="left:33px;top:615px;width:422px"></div>
      <div class="rule-end" style="left:453px;top:612px"></div>
      <div class="oval oval--hours">FLEXIBLE<br>HOURS<br>7 DAYS A<br>WEEK</div>
      <div class="abs contact" style="left:57px;top:623px;font-size:10px"><span class="social-icon"></span>SimpleGlowSunnyBay&nbsp;&nbsp;&nbsp;<span class="social-icon social-icon--round"></span>simpleglowsunnybay</div>
      <div class="abs contact" style="left:57px;top:647px">Palm Reach, Sunny Bay | Ph: 0400 123 987</div>
    </footer>
  </main>

  <div class="ornament-area" role="img" aria-label="Large red heart ornament topped with three stacked dots"></div>
</body>
</html>
```